Whiskey Glass Packaging Design Project

I require a package design for my products - Whiskey Tasting glasses ( Set of 4) I will be selling on the Brevora USA platform. Must be of high quality, something that the customer will be very impressed with after opening once it arrives at their doorstop. To get an idea of competition please take a look on Brevora.com and do a search on Whiskey Glasses - Scotch Glasses. The competition is very good so we require something that will be better than them. We have a home and kitchen brand that caters to an audience that appreciate fine whiskey / oak barrels / cigars ... I can provide logo and content to be placed on box as well as dine line.

Target Market(s)

Men who love all things about Whiskey / Business / Cigars. Men / Women / Wives / Husbands who are looking to buy gifts for Husband / Partner .

Requirements
Must have
• On one side of the box we would like for the following wording to be included.
The KERAVIND snifter glass is one of the ideal glasses that all enthusiasts will swear by. The glass is a type of stemware, a short - stemmed glass whose vessel has a wide bottom and a relatively narrow top. It is mostly used to serve aged brown Scotch / Whiskey, Bourbon and Brandy.
It's simply a matter of raising the glass to take in a whiff of the aromas before taking a sip. We hope the graceful design of this KERAVIND Whiskey glass adds a nice touch of class to the presentation of your favourite drop ! Enjoy !
Nice to have
• Elegant, soothing and relaxing feel.
Should not have
• Nothing aggressive, racist, homosexual / anti gay .

```html
<!DOCTYPE html>
<html lang="en">
<head>
<meta charset="utf-8">
<title>KERAVIND Snifter Glasses – Box Dieline 170x170x110mm</title>
<link rel="stylesheet" href="https://fonts.googleapis.com/css2?family=Montserrat:wght@300;400;500&family=Source+Sans+3:wght@400;700&family=Tinos&display=swap">
<style>
  :root {
    --paper: #ffffff;
    --box-black: #000000;
    --dieline: #1ba6e0;
    --accent-orange: #e8891c;
    --ink-dark: #1a1208;
    --ink-light: #ffffff;
    --gold-strip: #f0c21e;
  }
  html, body {
    margin: 0;
    padding: 0;
    width: 1200px;
    height: 638px;
    overflow: hidden;
    background: var(--paper);
  }
  .dieline-sheet {
    display: block;
    width: 1200px;
    height: 638px;
  }
  .size-label {
    font-family: "Tinos", serif;
    font-size: 84px;
    fill: #111;
  }
  .cut-line {
    fill: none;
    stroke: var(--dieline);
    stroke-width: 3;
    stroke-linejoin: round;
  }
  .lid-title {
    font-family: "Montserrat", sans-serif;
    font-weight: 400;
    font-size: 30px;
    letter-spacing: 6px;
    fill: var(--ink-light);
    text-anchor: middle;
  }
  .lid-subtitle {
    font-family: "Montserrat", sans-serif;
    font-weight: 400;
    font-size: 17px;
    letter-spacing: 4px;
    fill: var(--ink-light);
    text-anchor: middle;
  }
  .lid-brand {
    font-family: "Montserrat", sans-serif;
    font-weight: 400;
    font-size: 38px;
    letter-spacing: 10px;
    fill: var(--accent-orange);
    text-anchor: middle;
  }
  .front-brand {
    font-family: "Montserrat", sans-serif;
    font-weight: 500;
    font-size: 40px;
    letter-spacing: 10px;
    fill: var(--ink-dark);
    text-anchor: middle;
  }
  .front-caption {
    font-family: "Montserrat", sans-serif;
    font-weight: 400;
    font-size: 17px;
    letter-spacing: 4px;
    fill: var(--ink-light);
    text-anchor: middle;
  }
  .side-copy {
    font-family: "Source Sans 3", sans-serif;
    font-size: 8.2px;
    fill: var(--ink-dark);
  }
  .side-copy .brand-name { font-weight: 700; }
</style>
</head>
<body>
<svg class="dieline-sheet" viewBox="0 0 2560 1361" xmlns="http://www.w3.org/2000/svg">
  <defs>
    <linearGradient id="gold-panel" x1="0" y1="0" x2="1" y2="1">
      <stop offset="0" stop-color="#f6cf3a"/>
      <stop offset="0.35" stop-color="#ecbd25"/>
      <stop offset="0.7" stop-color="#b8772f"/>
      <stop offset="1" stop-color="#e6b53a"/>
    </linearGradient>
    <linearGradient id="gold-panel-light" x1="0" y1="0" x2="1" y2="1">
      <stop offset="0" stop-color="#e9b92a"/>
      <stop offset="0.25" stop-color="#fbdc5a"/>
      <stop offset="0.55" stop-color="#e6b627"/>
      <stop offset="1" stop-color="#c38a34"/>
    </linearGradient>
    <linearGradient id="gold-edge" x1="0" y1="0" x2="0" y2="1">
      <stop offset="0" stop-color="#f8d84e"/>
      <stop offset="1" stop-color="#b06f2a"/>
    </linearGradient>
    <linearGradient id="photo-tone" x1="0" y1="0" x2="0" y2="1">
      <stop offset="0" stop-color="#f4f4f2"/>
      <stop offset="0.6" stop-color="#e8c88a"/>
      <stop offset="1" stop-color="#d7d7d4"/>
    </linearGradient>
  </defs>

  <!-- size heading -->
  <text class="size-label" x="195" y="116">170x170x110mm</text>

  <!-- artwork background -->
  <rect class="print-edge" x="122" y="295" width="6" height="770" fill="url(#gold-edge)"/>
  <rect class="box-body" x="127" y="148" width="2403" height="1185" fill="var(--box-black)"/>

  <!-- gold hairline strips -->
  <rect class="gold-strip" x="136" y="541" width="2376" height="14" fill="var(--gold-strip)"/>
  <rect class="gold-strip" x="136" y="918" width="2376" height="14" fill="var(--gold-strip)"/>

  <!-- gold wrap band -->
  <rect x="127" y="607" width="18" height="268" fill="url(#gold-panel)"/>
  <rect x="2518" y="607" width="12" height="268" fill="url(#gold-panel)"/>
  <g class="front-panel" role="img" aria-label="Gold panel with line drawing of snifter glass outlines">
    <rect x="160" y="607" width="575" height="268" fill="url(#gold-panel)"/>
  </g>
  <rect class="side-panel" x="750" y="607" width="575" height="268" fill="url(#gold-panel-light)"/>
  <g class="front-panel" role="img" aria-label="Gold panel with line drawing of snifter glass outlines">
    <rect x="1340" y="607" width="573" height="268" fill="url(#gold-panel)"/>
  </g>
  <rect class="side-panel" x="1930" y="607" width="575" height="268" fill="url(#gold-panel)"/>

  <!-- lid: product title -->
  <text class="lid-title" x="449" y="388">SNIFTER</text>
  <text class="lid-subtitle" x="449" y="405">WHISKEY TASTING GLASSES</text>
  <text class="lid-subtitle" x="449" y="422">(SET OF 4)</text>
  <line x1="383" y1="446" x2="515" y2="446" stroke="#666" stroke-width="1.5"/>
  <rect x="445" y="442" width="8" height="8" fill="var(--accent-orange)" transform="rotate(45 449 446)"/>

  <!-- lid: brand, set upside down -->
  <text class="lid-brand" x="1627" y="342" transform="rotate(180 1627 355)">KERAVIND</text>

  <!-- front faces -->
  <text class="front-brand" x="449" y="792">KERAVIND</text>
  <text class="front-caption" x="449" y="902">WHISKEY TASTING GLASSES &#160;&#160; (SET OF 4)</text>
  <text class="front-brand" x="1630" y="792">KERAVIND</text>
  <text class="front-caption" x="1627" y="902">WHISKEY TASTING GLASSES &#160;&#160; (SET OF 4)</text>

  <!-- side face: photo area and copy -->
  <polygon role="img" aria-label="Photo of four snifter glasses with whiskey" points="2090,670 2165,745 2090,820 2015,745" fill="url(#photo-tone)"/>
  <text class="side-copy" x="2193" y="684">
    <tspan x="2193" y="684">The <tspan class="brand-name">KERAVIND</tspan> snifter glass is one of the ideal glasses</tspan>
    <tspan x="2193" y="697.5">that all enthusiasts will swear by. The glass is a type of stemware,</tspan>
    <tspan x="2193" y="711">a short - stemmed glass whose vessel has a wide bottom and a</tspan>
    <tspan x="2193" y="724.5">relatively narrow top. It is mostly used to serve aged</tspan>
    <tspan x="2193" y="738">brown Scotch / Whiskey, Bourbon and Brandy.</tspan>
    <tspan x="2193" y="765">It's simply a matter of raising the glass to take in a whiff of the</tspan>
    <tspan x="2193" y="778.5">aromas before taking a sip. We hope the graceful design of this</tspan>
    <tspan x="2193" y="792"><tspan class="brand-name">KERAVIND</tspan> Whiskey glass adds a nice touch of class to the</tspan>
    <tspan x="2193" y="805.5">presentation of your favourite drop ! Enjoy !</tspan>
  </text>

  <!-- dieline -->
  <g class="cut-line">
    <!-- glue flap and main creases -->
    <path d="M154,548 L67,598 V878 L154,928"/>
    <line x1="154" y1="548" x2="2510" y2="548"/>
    <line x1="154" y1="928" x2="2510" y2="928"/>
    <line x1="2510" y1="548" x2="2510" y2="928"/>

    <!-- tuck panels -->
    <rect x="154" y="249" width="589" height="977"/>
    <rect x="1334" y="249" width="589" height="977"/>
    <path d="M189,252 V198 L222,165 H425 L442,182 V202 A7,7 0 0 0 456,202 V182 L473,165 H676 L709,198 V252"/>
    <path d="M189,1222 V1276 L222,1310 H425 L442,1293 V1273 A7,7 0 0 1 456,1273 V1293 L473,1310 H676 L709,1276 V1222"/>
    <path d="M1368,252 V198 L1401,165 H1604 L1621,182 V202 A7,7 0 0 0 1635,202 V182 L1652,165 H1855 L1888,198 V252"/>
    <path d="M1368,1222 V1276 L1401,1310 H1604 L1621,1293 V1273 A7,7 0 0 1 1635,1273 V1293 L1652,1310 H1855 L1888,1276 V1222"/>

    <!-- dust flap panels -->
    <path d="M754,545 V200 Q754,172 782,172 H1294 Q1322,172 1322,200 V545"/>
    <line x1="754" y1="258" x2="1322" y2="258"/>
    <rect x="1031" y="215" width="14" height="302" rx="7"/>
    <path d="M754,932 V1277 Q754,1305 782,1305 H1294 Q1322,1305 1322,1277 V932"/>
    <line x1="754" y1="1218" x2="1322" y2="1218"/>
    <rect x="1031" y="960" width="14" height="300" rx="7"/>

    <path d="M1933,545 V200 Q1933,172 1961,172 H2473 Q2501,172 2501,200 V545"/>
    <line x1="1933" y1="258" x2="2501" y2="258"/>
    <rect x="2210" y="215" width="14" height="302" rx="7"/>
    <path d="M1933,932 V1277 Q1933,1305 1961,1305 H2473 Q2501,1305 2501,1277 V932"/>
    <line x1="1933" y1="1218" x2="2501" y2="1218"/>
    <rect x="2210" y="960" width="14" height="300" rx="7"/>
  </g>
</svg>
</body>
</html>
```